Help make our corporate website modern and cool with graphical elements and icons

We are makers of cloud infrastructure software (www.nimbrotek.com) and our target audience is developers. Developers generally want text and icons, they don't care for photos. They want good usability and easy-to-find information. Think forkhive.com, cloud.zephyrqa.com, www.stackmoor.com, pallork.com for reference.

Your challenge will be to modernize the site and make it look "cool" from a developer's point-of-view while still keeping the basic site structure. You can add graphical elements that make the pages come more alive, suggest different layout options, and incorporate icons that we've recently developed (I've attached them for your review). We will keep the Nimbrotek blue and gray, but you are free to add complementary colors in your designs to help spice up the page. See the complementary colors we've used in the icons package.

A successful design will keep the core identity of our website but will make the pages more exciting and compelling to visit, and make the visitor want to scroll and click to dive in deeper into the site. I also want to see additional mock-ups for the main landing pages (Why Nimbrotek, Products, Community, and a new landing page for Resources).

We use WordPress and the Q theme, so if you have familiarity with that theme and its capabilities, even better.

Target Market(s)

Mobile and Web application developers from larger organizations. Developers typically don't like stock images of people or landscapes, they usually just want the information they're looking for presented in a clean and organized way. That said, they do like it if an icon or design element helps them visualize the information. So the design should be useful and necessary to the info provided.

Industry/Entity Type

Computer Software

Number of Pages Required

5+ page

Font styles to use
Sans Serif
Other font styles liked:
• We use Lato as our main font

Colors

Designer to choose colors to be used in the design.

Requirements
Must have
• Must haves:
• - clean and modern design, not too busy but still visually engaging
• - keep the core identity of the site while adding graphical elements/icons
• - use either the hexagons from the icons or incorporate the venn diagram shape somehow from https://www.nimbrotek.com/why-nimbrotek/
• - shapes and icons are preferred over photos or stock "tech" images
• - should keep the nimbrotek blue and gray but can have complementary accent colors (see the icon colors that I've attached)
• - you can use the attached icons
• - make the information appealing to view, scroll and click through
• - design must not interfere with navigation or readability, must complement and be appropriate for the specific information shown
• - use pallork.com and cloud.zephyrqa.com for reference
Nice to have
• nice to haves:
• - familiarity with Zephyrqa Run Engine and cloud computing
• - easy to implement on WordPress, familiarity with Q theme a plus
• - ability to identify with app developers
Should not have
• - unfortunately, stock photos of people or landscapes won't work
• - don't use clip art of clouds or other stock images of high tech
• - don't make it too busy, we are looking for clean and modern

```html
<!DOCTYPE html>
<html lang="en">
<head>
<meta charset="utf-8">
<title>Nimbrotek — Multi cloud native</title>
<link rel="stylesheet" href="https://fonts.googleapis.com/css2?family=Lato:wght@300;400;700;900&display=swap">
<style>
:root{
  --brand:#1e9ded;
  --brand-deep:#1173d4;
  --band-top:#2a93e6;
  --band-bottom:#1a7bd3;
  --benefit-top:#1da3ee;
  --benefit-bottom:#1683dc;
  --ink:#333;
  --muted:#666;
  --soft:#f0f0f0;
  --strip:#ececec;
  --footer:#4b4b4b;
  --footer-base:#3e3e3e;
  --white:#fff;
}
*{box-sizing:border-box;margin:0;padding:0}
html,body{width:1200px;height:3523px;overflow:hidden}
body{font-family:"Lato",sans-serif;color:var(--ink);background:var(--white);position:relative}
section,header,footer{position:absolute;left:0;width:1200px}

/* header */
.site-header{top:0;height:94px;background:var(--brand)}
.brand{position:absolute;left:128px;top:24px;font-size:38px;font-weight:400;color:var(--white);letter-spacing:.5px}
.main-nav{position:absolute;left:386px;top:38px;display:flex;gap:38px}
.main-nav a{color:var(--white);text-decoration:none;font-size:15px;font-weight:700;letter-spacing:.3px}
.contact-btn{position:absolute;left:948px;top:24px;width:132px;height:44px;background:var(--brand-deep);color:var(--white);font-size:13px;font-weight:700;display:flex;align-items:center;justify-content:center;text-decoration:none}

/* hero */
.hero{top:94px;height:517px;background:var(--white)}
.hero h1{position:absolute;top:44px;width:100%;text-align:center;font-weight:400;font-size:35px;line-height:45px;color:#444}
.try-btn{position:absolute;left:520px;top:155px;width:152px;height:40px;background:var(--brand);color:var(--white);font-weight:700;font-size:19px;display:flex;align-items:center;justify-content:center;text-decoration:none}
.hero-art{position:absolute;left:247px;top:205px;width:693px;height:265px;border-radius:30px;background:radial-gradient(ellipse at center,#e7f1fa 0%,#f5f8fb 60%,#fff 100%)}
.slider-arrow{position:absolute;top:250px;width:50px;height:50px;border:2px solid #777;border-radius:50%}
.slider-arrow.prev{left:76px}.slider-arrow.next{left:1062px}

/* provider strip */
.providers{top:611px;height:98px;background:var(--strip);display:flex;justify-content:center;align-items:center;gap:44px}
.provider{font-size:15px;font-weight:700;color:#8a8a8a;display:flex;align-items:center;gap:7px}
.provider i{width:12px;height:12px;background:#9a9a9a;display:inline-block}

/* capability band */
.capabilities{top:709px;height:428px;background:linear-gradient(180deg,var(--band-top),var(--band-bottom))}
.capabilities h2{position:absolute;top:48px;width:100%;text-align:center;color:var(--white);font-weight:400;font-size:28px;line-height:34px}
.cap-card{position:absolute;top:141px;width:237px;height:219px;border:1px solid rgba(255,255,255,.8);text-align:center;color:var(--white);padding:0 20px}
.cap-card svg{margin-top:22px}
.cap-card h3{font-size:17px;font-weight:700;margin-top:12px}
.cap-card p{font-size:12px;line-height:16px;margin-top:10px;opacity:.95}

/* cost */
.cost{top:1137px;height:425px;background:var(--white)}
.cost h2{position:absolute;left:122px;top:82px;font-size:29px;font-weight:400;color:#222}
.cost p{position:absolute;left:122px;width:440px;font-size:13px;line-height:20px;color:var(--muted)}
.learn-btn{position:absolute;left:117px;top:293px;width:183px;height:45px;border-radius:23px;background:var(--brand-deep);color:var(--white);font-size:13px;font-weight:700;display:flex;align-items:center;justify-content:center;text-decoration:none}
.cost-chart{position:absolute;left:679px;top:61px;width:371px;height:286px;box-shadow:0 4px 16px rgba(0,0,0,.18);background:linear-gradient(180deg,#f4f7fa 0%,#dde9f5 55%,#bcd6ef 100%)}

/* steps */
.steps{top:1562px;height:449px;background:var(--soft);border-top:1px solid #ddd}
.steps h2{position:absolute;top:63px;width:100%;text-align:center;font-size:28px;font-weight:400;color:#222}
.steps svg.route{position:absolute;left:0;top:0}
.step{position:absolute;top:120px;width:244px;height:244px;border-radius:50%;background:var(--white);box-shadow:0 6px 22px rgba(0,0,0,.12);text-align:center}
.step svg{margin-top:44px}
.step span{display:block;margin-top:14px;color:var(--brand);font-weight:700;font-size:19px}

/* clients */
.clients{top:2011px;height:268px;background:var(--white)}
.clients h2{position:absolute;top:68px;width:100%;text-align:center;font-size:22px;font-weight:400;color:#444}
.client-row{position:absolute;top:142px;left:0;width:100%;display:flex;justify-content:center;gap:70px;align-items:center;height:60px}
.client{font-size:26px;font-weight:700;color:#777}

/* benefits */
.benefits{top:2279px;height:434px;background:linear-gradient(180deg,var(--benefit-top),var(--benefit-bottom))}
.benefits h2{position:absolute;top:56px;width:100%;text-align:center;color:var(--white);font-size:26px;font-weight:400;line-height:31px}
.benefit{position:absolute;width:400px;color:var(--white)}
.benefit svg{position:absolute;left:0;top:0}
.benefit h3{margin-left:95px;font-size:19px;font-weight:700}
.benefit p{margin-left:95px;margin-top:6px;font-size:12px;line-height:16px;width:300px}

/* testimonial */
.testimonial{top:2713px;height:463px;background:var(--white)}
.video{position:absolute;left:127px;top:82px;width:465px;height:280px;background:linear-gradient(135deg,#5a5f66,#2c2f33)}
.play{position:absolute;left:202px;top:110px;width:60px;height:60px;border-radius:50%;background:rgba(255,255,255,.85)}
.play:after{content:"";position:absolute;left:24px;top:18px;border-left:18px solid #333;border-top:12px solid transparent;border-bottom:12px solid transparent}
.quote-box{position:absolute;left:550px;top:59px;width:514px;height:277px;border:2px solid #3a8fe0;background:var(--white);padding:36px 0 0 78px}
.quote-box h3{color:var(--brand);font-size:20px;font-weight:400}
.quote-box blockquote{margin-top:18px;width:360px;font-size:17px;line-height:26px;color:#444}
.author{margin-top:22px;display:flex;align-items:center;gap:10px}
.author .avatar{width:40px;height:40px;border-radius:50%;background:#555}
.author b{display:block;font-size:12px;font-weight:400;color:#222}
.author small{font-size:12px;color:var(--brand)}

/* footer */
.site-footer{top:3176px;height:277px;background:var(--footer);color:var(--white)}
.foot-col{position:absolute;top:57px}
.foot-col h4{font-size:19px;font-weight:400;letter-spacing:.3px;margin-bottom:16px}
.foot-col a{display:block;color:#ddd;font-size:13px;text-decoration:none;line-height:29px}
.social{display:flex;gap:8px}
.social span{width:40px;height:40px;border:2px solid #ccc;border-radius:50%;font-size:8px;display:flex;align-items:center;justify-content:center;color:#ddd}
.copyright{position:absolute;top:3453px;left:0;width:1200px;height:70px;background:var(--footer-base);color:#bbb;font-size:12px;display:flex;align-items:center;justify-content:center}
</style>
</head>
<body>

<header class="site-header">
  <div class="brand">Nimbrotek</div>
  <nav class="main-nav">
    <a href="#">WHY NIMBROTEK</a><a href="#">PRODUCTS</a><a href="#">COMMUNITY</a><a href="#">RESOURCES</a>
  </nav>
  <a class="contact-btn" href="#">CONTACT US</a>
</header>

<section class="hero">
  <h1>Multi cloud native. Serverless by design.<br>NoOps as a first principle.</h1>
  <a class="try-btn" href="#">Try it Free</a>
  <div class="hero-art" role="img" aria-label="Line illustration of clouds, gears, pipes and devices connected across providers"></div>
  <svg class="slider-arrow prev" viewBox="0 0 50 50"><path d="M28 16 L19 25 L28 34" fill="none" stroke="#777" stroke-width="2.5"/></svg>
  <svg class="slider-arrow next" viewBox="0 0 50 50"><path d="M22 16 L31 25 L22 34" fill="none" stroke="#777" stroke-width="2.5"/></svg>
</section>

<section class="providers">
  <div class="provider"><i></i>Veltrax</div>
  <div class="provider"><i></i>Quorvane</div>
  <div class="provider"><i></i>On-premises</div>
  <div class="provider"><i></i>Orbisk Web Services</div>
  <div class="provider"><i></i>Zephyrqa Cloud Platform</div>
  <div class="provider"><i></i>Tessum Cloud</div>
  <div class="provider"><i></i>Kerrowan Cloud</div>
</section>

<section class="capabilities">
  <h2>Nimbrotek enables serverless development<br>with application portability</h2>
  <div class="cap-card" style="left:117px">
    <svg width="80" height="72" viewBox="0 0 80 72"><polygon points="20,0 60,0 80,36 60,72 20,72 0,36" fill="#3ab0f2"/><ellipse cx="40" cy="24" rx="14" ry="5" fill="none" stroke="#fff" stroke-width="2"/><path d="M26 24v22c0 3 6 5 14 5s14-2 14-5V24M26 35c0 3 6 5 14 5s14-2 14-5" fill="none" stroke="#fff" stroke-width="2"/></svg>
    <h3>Multi Cloud Migration</h3>
    <p>Migrate between major public cloud providers with no code changes, for cost-savings and</p>
  </div>
  <div class="cap-card" style="left:362px">
    <svg width="80" height="72" viewBox="0 0 80 72"><polygon points="20,0 60,0 80,36 60,72 20,72 0,36" fill="#3ab0f2"/><path d="M24 46h32a9 9 0 0 0 0-18 13 13 0 0 0-25-2 10 10 0 0 0-7 20z" fill="none" stroke="#fff" stroke-width="2"/><circle cx="40" cy="38" r="5" fill="none" stroke="#fff" stroke-width="2"/></svg>
    <h3>Hybrid Cloud</h3>
    <p>Run cloud-native apps in public cloud and on premises, even in isolated</p>
  </div>
  <div class="cap-card" style="left:604px">
    <svg width="80" height="72" viewBox="0 0 80 72"><polygon points="20,0 60,0 80,36 60,72 20,72 0,36" fill="#3ab0f2"/><rect x="24" y="20" width="32" height="32" fill="none" stroke="#fff" stroke-width="2"/><path d="M24 31h32M24 42h32M29 26h4M29 37h4M29 47h4" stroke="#fff" stroke-width="2"/></svg>
    <h3>Serverless Platform</h3>
    <p>Increase developer productivity using high-level APIs on a platform</p>
  </div>
  <div class="cap-card" style="left:846px">
    <svg width="80" height="72" viewBox="0 0 80 72"><polygon points="20,0 60,0 80,36 60,72 20,72 0,36" fill="#3ab0f2"/><rect x="32" y="16" width="16" height="40" rx="4" fill="none" stroke="#fff" stroke-width="2"/><circle cx="40" cy="25" r="4" fill="#fff"/><circle cx="40" cy="36" r="4" fill="#fff"/><circle cx="40" cy="47" r="4" fill="#fff"/></svg>
    <h3>NoOps</h3>
    <p>Escape cloud lock-in, minimize costs, and future-proof your application</p>
  </div>
</section>

<section class="cost">
  <h2>Calculate the Cost to Migrate Clouds</h2>
  <p style="top:136px">Fusce ultricies orci ac feugiat suscipit leo massa sodales velit et scelerisque mi tortor at ipsum aliquam augue bibendum accumsan vestibulum ut commodo a m Morbi ornare</p>
  <p style="top:209px">avida elit Integer congue augue et malesuada iaculis ipsum dui aliquet felis at cursus magna nisl nec elit Praesent elementum elit</p>
  <a class="learn-btn" href="#">LEARN MORE</a>
  <div class="cost-chart" role="img" aria-label="Screen showing a rising blue bar and line chart of cloud costs"></div>
</section>

<section class="steps">
  <h2>Get started in 3 easy steps</h2>
  <svg class="route" width="1200" height="449" viewBox="0 0 1200 449">
    <path d="M183 310 A152 152 0 1 1 462 300 C480 420 700 420 728 300 A152 152 0 1 1 1028 288" fill="none" stroke="#4aa8ea" stroke-width="2"/>
    <path d="M720 312 L728 298 L738 310" fill="#4aa8ea"/>
    <circle cx="183" cy="310" r="6" fill="#4aa8ea"/>
    <circle cx="1028" cy="288" r="6" fill="#4aa8ea"/>
  </svg>
  <div class="step" style="left:200px">
    <svg width="76" height="68" viewBox="0 0 76 68"><polygon points="19,0 57,0 76,34 57,68 19,68 0,34" fill="#1e88d8"/><circle cx="38" cy="34" r="9" fill="none" stroke="#fff" stroke-width="2"/><path d="M38 16v9M38 43v9M20 34h9M47 34h9" stroke="#fff" stroke-width="2"/></svg>
    <span>Install Nimbrotek</span>
  </div>
  <div class="step" style="left:482px">
    <svg width="76" height="68" viewBox="0 0 76 68"><polygon points="19,0 57,0 76,34 57,68 19,68 0,34" fill="#1e88d8"/><path d="M24 22h4M32 22h20M24 34h4M32 34h20M24 46h4M32 46h20" stroke="#fff" stroke-width="2.5"/></svg>
    <span>Write your app</span>
  </div>
  <div class="step" style="left:770px;top:110px">
    <svg width="76" height="68" viewBox="0 0 76 68"><polygon points="19,0 57,0 76,34 57,68 19,68 0,34" fill="#1e88d8"/><circle cx="27" cy="27" r="4" fill="#fff"/><circle cx="38" cy="27" r="4" fill="#fff"/><circle cx="49" cy="27" r="4" fill="#fff"/><rect x="22" y="38" width="32" height="10" rx="2" fill="#fff"/></svg>
    <span>Run your app</span>
  </div>
</section>

<section class="clients">
  <h2>Successful startups and innovative companies choose Nimbrotek</h2>
  <div class="client-row">
    <div class="client">Lumeno</div>
    <div class="client">Brevixa</div>
    <div class="client">Ostrell</div>
    <div class="client">Terrafund</div>
    <div class="client">Palvo</div>
  </div>
</section>

<section class="benefits">
  <h2>Nimbrotek benefits developers, operations, and the organization<br>with a serverless platform for multi cloud deployment.</h2>
  <div class="benefit" style="left:155px;top:168px">
    <svg width="80" height="72" viewBox="0 0 80 72"><polygon points="20,1 60,1 79,36 60,71 20,71 1,36" fill="none" stroke="#fff" stroke-width="1.5"/><circle cx="40" cy="36" r="5" fill="none" stroke="#fff" stroke-width="1.5"/><circle cx="28" cy="26" r="3" fill="#fff"/><circle cx="52" cy="26" r="3" fill="#fff"/><circle cx="28" cy="46" r="3" fill="#fff"/><circle cx="52" cy="46" r="3" fill="#fff"/></svg>
    <h3>Marlow Trade Co</h3>
    <p>Cloud migration from Zephyrqa Run Engine to mainland China with no modifications or proxy servers.</p>
  </div>
  <div class="benefit" style="left:620px;top:168px">
    <svg width="80" height="72" viewBox="0 0 80 72"><polygon points="20,1 60,1 79,36 60,71 20,71 1,36" fill="none" stroke="#fff" stroke-width="1.5"/><rect x="30" y="26" width="20" height="20" fill="none" stroke="#fff" stroke-width="1.5"/><path d="M34 22v4M40 22v4M46 22v4M34 46v4M40 46v4M46 46v4" stroke="#fff" stroke-width="1.5"/></svg>
    <h3>Dockaro</h3>
    <p>Cloud-native application enabled for on-premises deployments for better security and control.</p>
  </div>
  <div class="benefit" style="left:155px;top:278px">
    <svg width="80" height="72" viewBox="0 0 80 72"><polygon points="20,1 60,1 79,36 60,71 20,71 1,36" fill="none" stroke="#fff" stroke-width="1.5"/><rect x="26" y="26" width="28" height="20" fill="none" stroke="#fff" stroke-width="1.5"/><path d="M26 36h28" stroke="#fff" stroke-width="1.5"/></svg>
    <h3>Fennly</h3>
    <p>Hybrid cloud implementation for paid and freemium customers to reduce overall cloud costs.</p>
  </div>
  <div class="benefit" style="left:620px;top:278px">
    <svg width="80" height="72" viewBox="0 0 80 72"><polygon points="20,1 60,1 79,36 60,71 20,71 1,36" fill="none" stroke="#fff" stroke-width="1.5"/><path d="M40 22l12 5v9c0 8-6 13-12 15-6-2-12-7-12-15v-9z" fill="none" stroke="#fff" stroke-width="1.5"/></svg>
    <h3>Trelmark Retail</h3>
    <p>Cloud migration to Veltrax Cloud for improved performance and reliability and developer flexibility.</p>
  </div>
</section>

<section class="testimonial">
  <div class="video" role="img" aria-label="Video still of a speaker talking about the platform"><div class="play"></div></div>
  <div class="quote-box">
    <h3>Testimonials</h3>
    <blockquote>“With Nimbrotek you can run your Zephyrqa Run Engine app on any physical or cloud infrastructure, wherever you want.”</blockquote>
    <div class="author">
      <div class="avatar" role="img" aria-label="Portrait of the quoted director"></div>
      <div><b>CORIN ABATE</b><small>Director, Solutions | Zephyrqa Cloud Platform</small></div>
    </div>
  </div>
</section>

<footer class="site-footer">
  <div class="foot-col" style="left:122px"><h4>COMPANY</h4><a href="#">Home</a><a href="#">About Us</a><a href="#">Why Us</a><a href="#">Testimonials</a></div>
  <div class="foot-col" style="left:345px"><h4>SUBLINKS</h4><a href="#">Get Started</a><a href="#">Our Products</a><a href="#">Community</a><a href="#">Try Now</a></div>
  <div class="foot-col" style="left:599px"><h4>RESOURCES</h4><a href="#">Partners</a><a href="#">Press</a><a href="#">Team</a><a href="#">Contact Us</a></div>
  <div class="foot-col" style="left:836px"><h4>FOLLOW US</h4>
    <div class="social"><span>Chirp</span><span>Facet</span><span>Linkr</span><span>Plusly</span></div>
  </div>
</footer>
<div class="copyright">© 2018 Company Name. All right reserved</div>

</body>
</html>
```